Mark Dunvale actor business cards

I need unique and interesting business cards that have my headshot photo, my name, tagline/position/skills, contact info, preferred pronouns (he, him, his), and social media handles. These need to be memorable networking tools to hand out at events that stand out. I am an actor that works in theatre, film, and TV and usually play darker dramatic roles, though it doesn't have to necessarily need to be reflected in the design, but I am not a light, comedic actor. In my email tagline, My position/skills are "Actor, storyteller, theatre maker."

Target Market(s)

Casting directors, film and television community, theatre community.

Industry/Entity Type

Performing Art

Contact Information for Business Card

Mark Dunvale. Pronouns: he, him, his. Contact info: (555)-318-7406, Markdunvale.example, markdunvale@mailbox.example. Talent representation: Corvanti Talent Agency. Social Media: Friendbook page, chirpit and snapgram: @MarkDunvaleActs. Company Member of Larkhollow Theatre Company.

Font styles to use
Serif
Decorative

Colors

Designer to choose colors to be used in the design.

Requirements
Must have
• Headshot photo, name, tagline, preferred pronouns, contact info, Social media handle, talent agency logo, larkhollow theatre company logo. Both logos should be smaller than my name. Under or near Larkhollow logo, it should say "Company Member"
Nice to have
• I would like to have the photo, my name, tagline, and maybe pronouns on one side, and all contact info, and social media, and talent agency logo on the other. I would like the style to reflect my type which is a little more serious and somewhat darker, and definitely not comedic.
Should not have
• No extraneous theatre lights, camera, or film, etc. clip art or photos. Use solid backgrounds or photos provided.

```html
<!DOCTYPE html>
<html lang="en">
<head>
<meta charset="utf-8">
<title>Mark Dunvale – Business Cards</title>
<link rel="stylesheet" href="https://fonts.googleapis.com/css2?family=Anton&family=Montserrat:wght@400;500&display=swap">
<style>
  :root {
    --bg: #e9e6e1;
    --card-black: #101010;
    --card-dark: #1e1e1e;
    --card-mid: #2c2c2c;
    --band: #0a0a0a;
    --band-edge: #3a3a3a;
    --icon-tile: #5a5a5a;
    --text-white: #ffffff;
    --text-soft: #d8d8d8;
    --text-muted: #8c8c8c;
    --rule: #6a6a6a;
    --photo-top: #7fb1b3;
    --photo-mid: #5d7fa6;
    --photo-low: #3d4f6e;
  }
  * { box-sizing: border-box; margin: 0; padding: 0; }
  html, body { width: 771px; height: 1200px; overflow: hidden; }
  body {
    background: var(--bg);
    font-family: "Montserrat", sans-serif;
    display: flex;
    align-items: center;
    justify-content: center;
    gap: 31px;
  }
  .card {
    position: relative;
    width: 340px;
    height: 595px;
    border-radius: 18px;
    overflow: hidden;
    box-shadow: 0 10px 30px rgba(0,0,0,.25);
  }

  /* Front */
  .card-front { background: var(--card-black); }
  .headshot {
    position: absolute;
    inset: 0;
    background: linear-gradient(180deg, var(--photo-top) 0%, var(--photo-mid) 45%, var(--photo-low) 68%, var(--card-black) 88%);
  }
  .front-name {
    position: absolute;
    left: 26px; bottom: 74px;
    font-family: "Anton", sans-serif;
    font-size: 42px;
    font-weight: 400;
    letter-spacing: 1px;
    color: var(--text-soft);
    text-transform: uppercase;
    line-height: 1;
  }
  .front-tagline {
    position: absolute;
    left: 26px; bottom: 48px;
    font-size: 14px;
    color: var(--text-muted);
  }
  .front-pronouns {
    position: absolute;
    left: 26px; bottom: 26px;
    font-size: 11px;
    letter-spacing: 1px;
    color: var(--text-muted);
  }

  /* Back */
  .card-back {
    background: linear-gradient(135deg, var(--card-mid) 0%, var(--card-dark) 45%, var(--card-black) 100%);
  }
  .side-band {
    position: absolute;
    left: 34px; top: 0; bottom: 0;
    width: 56px;
    background: var(--band);
    border-right: 6px solid var(--band-edge);
  }
  .back-name {
    position: absolute;
    right: 22px; top: 40px;
    font-family: "Anton", sans-serif;
    font-size: 36px;
    font-weight: 400;
    letter-spacing: 1px;
    color: var(--text-white);
    text-transform: uppercase;
    line-height: 1;
  }
  .back-tagline {
    position: absolute;
    right: 22px; top: 86px;
    font-size: 12px;
    color: var(--text-soft);
  }
  .representation {
    position: absolute;
    left: 110px; top: 130px;
    font-size: 12px;
    color: var(--text-white);
  }
  .agency {
    position: absolute;
    right: 22px; top: 156px;
    text-align: right;
    color: var(--text-white);
    font-size: 22px;
    line-height: 1;
  }
  .agency small { display: block; font-size: 8px; color: var(--text-soft); margin-top: 3px; }
  .contact-list { position: absolute; left: 0; top: 222px; width: 100%; list-style: none; }
  .contact-item { position: relative; height: 70px; }
  .contact-icon {
    position: absolute;
    left: 36px; top: 0;
    width: 50px; height: 50px;
    background: var(--icon-tile);
    display: flex; align-items: center; justify-content: center;
  }
  .contact-text {
    position: absolute;
    left: 108px; top: 8px;
    font-size: 13px;
    color: var(--text-white);
  }
  .contact-text.phone { font-size: 17px; top: 4px; }
  .contact-rule {
    position: absolute;
    left: 108px; top: 40px;
    width: 90px; height: 1px;
    background: var(--rule);
  }
  .company {
    position: absolute;
    left: 110px; top: 446px;
    color: var(--text-white);
  }
  .company-label {
    font-size: 9px;
    letter-spacing: 1px;
    text-transform: uppercase;
    color: var(--text-muted);
    margin-bottom: 5px;
  }
  .company-name {
    display: flex;
    align-items: center;
    gap: 6px;
    font-size: 11px;
    font-weight: 500;
  }
  .company-mark {
    width: 10px; height: 10px;
    background: var(--text-white);
    flex: none;
  }
  .social {
    position: absolute;
    left: 110px; bottom: 36px; right: 18px;
    color: var(--text-soft);
    font-size: 10px;
  }
  .social-names { display: flex; gap: 10px; color: var(--text-muted); margin-bottom: 6px; }
  .social-handle { font-size: 14px; color: var(--text-white); }
</style>
</head>
<body>
  <article class="card card-front">
    <div class="headshot" role="img" aria-label="Headshot photo of Mark Dunvale"></div>
    <h1 class="front-name">Mark Dunvale</h1>
    <p class="front-tagline">Actor, storyteller, theatre maker</p>
    <p class="front-pronouns">he / him / his</p>
  </article>

  <article class="card card-back">
    <div class="side-band"></div>
    <h2 class="back-name">Mark Dunvale</h2>
    <p class="back-tagline">Actor, storyteller, theatre maker</p>
    <p class="representation">Talent representation</p>
    <p class="agency">Corvanti<small>Talent Agency</small></p>

    <ul class="contact-list">
      <li class="contact-item">
        <span class="contact-icon">
          <svg width="24" height="24" viewBox="0 0 24 24"><path fill="#fff" d="M6.6 10.8a15.1 15.1 0 0 0 6.6 6.6l2.2-2.2c.3-.3.7-.4 1-.2 1.1.4 2.3.6 3.6.6.6 0 1 .4 1 1V20c0 .6-.4 1-1 1A17 17 0 0 1 3 4c0-.6.4-1 1-1h3.5c.6 0 1 .4 1 1 0 1.3.2 2.5.6 3.6.1.3 0 .7-.2 1z"/></svg>
        </span>
        <span class="contact-text phone">(555)-318-7406</span>
        <span class="contact-rule"></span>
      </li>
      <li class="contact-item">
        <span class="contact-icon">
          <svg width="24" height="24" viewBox="0 0 24 24"><rect x="3" y="6" width="18" height="12" fill="#fff"/><path d="M3 6l9 7 9-7" fill="none" stroke="#5a5a5a" stroke-width="1.5"/></svg>
        </span>
        <span class="contact-text">markdunvale@mailbox.example</span>
        <span class="contact-rule"></span>
      </li>
      <li class="contact-item">
        <span class="contact-icon">
          <svg width="24" height="24" viewBox="0 0 24 24" fill="none" stroke="#fff" stroke-width="1.6"><circle cx="12" cy="12" r="9"/><ellipse cx="12" cy="12" rx="4" ry="9"/><path d="M3 12h18M5 7h14M5 17h14"/></svg>
        </span>
        <span class="contact-text">Markdunvale.example</span>
        <span class="contact-rule"></span>
      </li>
    </ul>

    <div class="company">
      <p class="company-label">Company Member</p>
      <p class="company-name"><span class="company-mark"></span>Larkhollow Theatre Company</p>
    </div>

    <div class="social">
      <p class="social-names"><span>Friendbook</span><span>chirpit</span><span>snapgram</span></p>
      <p class="social-handle">@MarkDunvaleActs</p>
    </div>
  </article>
</body>
</html>
```